Flyer Design

A flyer to introduce our new business called Smilewagons on Wheels ,we are a mobile dental hygienist service based in the Teesside area of England.We use portable equipment to treat clients where they live or work Since may 2013 in the uk hygienists no longer need to work with a dentist ,therefore clients can now access dental hygiene care without seeing a dentist.We offer scale and polish ,oral hygiene advice .Our colours are pink,green and purple.we would like to stress the importance of a regular professional clean with the convenience of being treated at home

Target Market(s)

over 18 years of age who choose or need to have there scale and polish at home

Industry/Entity Type

Dental

Colors
e34297
9ccb3b
876aae

Requirements
Must have
• ,must have our logo and our contact details tel 07812460395 and email info@smilewagonsonwheels.co.uk
The hygienists names Moira Palfrey and Janet Ruddock
eye catching and colourful ,not to many words,but getting across we are for anyone who chooses or needs their treatment at home
Nice to have
• we would like the logo to be prominent ,our colours are pink ,green and purple .the font easy to read for older people
Should not have
• A lot of writing on the front the page ,

```html
<!DOCTYPE html>
<html lang="en">
<head>
<meta charset="utf-8">
<title>Smilewagons on Wheels – Flyer</title>
<link rel="stylesheet" href="https://fonts.googleapis.com/css2?family=Open+Sans:wght@400;600;700&family=Roboto+Condensed:wght@400&display=swap">
<style>
  :root{
    --pink:#e34297;
    --green:#9ccb3b;
    --green-dark:#5a9a2a;
    --purple:#876aae;
    --purple-deep:#5b3f8c;
    --purple-night:#4a3376;
    --paper:#ffffff;
    --stage:#e4e4e4;
  }
  *{box-sizing:border-box;margin:0;padding:0}
  html,body{width:928px;height:1200px;overflow:hidden}
  body{background:var(--stage);font-family:"Open Sans",Arial,sans-serif;position:relative}
  .flyer{position:absolute;top:337px;width:410px;height:525px;background:var(--paper);overflow:hidden;box-shadow:0 3px 10px rgba(0,0,0,.25)}
  .flyer--front{left:40px}
  .flyer--back{left:478px}
  .flyer__art{position:absolute;inset:0;width:410px;height:525px}
  .brand{position:absolute;left:14px;top:12px;width:150px;text-align:center}
  .brand__name{display:flex;align-items:center;justify-content:center;gap:6px;color:var(--pink);font-size:13px;font-weight:400}
  .brand__dot{width:9px;height:9px;border-radius:50%;background:var(--pink)}
  .brand__tagline{margin-top:26px;color:var(--green-dark);font-size:10.5px}
  .intro{position:absolute;left:0;right:0;top:327px;text-align:center;color:#fff;font-weight:600;font-size:15.5px;line-height:20px}
  .call{position:absolute;left:49px;top:410px;color:#fff;line-height:1;font-size:12.5px}
  .call__big{display:block;font-size:25px;font-weight:700;margin:-1px 0 -2px}
  .phone-btn{position:absolute;left:132px;top:398px;width:229px;height:66px;border:2px solid #fff;border-radius:8px;background:linear-gradient(#a6d85a,#5f9f2c);box-shadow:0 2px 4px rgba(0,0,0,.35);display:flex;align-items:center;color:#fff}
  .phone-btn__icon{width:46px;display:flex;justify-content:center}
  .phone-btn__rule{width:2px;height:48px;background:#fff}
  .phone-btn__number{padding-left:8px;font-family:"Roboto Condensed","Arial Narrow",sans-serif;font-size:31px;letter-spacing:.5px}
  .email{position:absolute;left:0;right:0;top:486px;text-align:center;color:#fff;font-size:11.5px;font-weight:600}
  .about{position:absolute;left:22px;right:22px;top:259px;color:#fff}
  .about__title{font-size:10px;font-weight:700;margin-bottom:8px}
  .about__text{font-size:7px;line-height:9px;margin-bottom:6px}
  .team{position:absolute;left:0;right:0;top:352px;text-align:center;color:#fff}
  .team__label{display:flex;align-items:center;justify-content:center;gap:4px;font-size:9.5px}
  .team__label::before,.team__label::after{content:"";width:58px;height:1px;background:#fff}
  .team__names{font-size:14px;font-weight:600;margin-top:1px}
</style>
</head>
<body>

<section class="flyer flyer--front">
  <svg class="flyer__art" viewBox="0 0 410 525">
    <defs>
      <linearGradient id="clinicTones" x1="0" y1="0" x2="1" y2="1">
        <stop offset="0" stop-color="#f2f0ee"/>
        <stop offset=".45" stop-color="#d9c3b6"/>
        <stop offset="1" stop-color="#7fb0d8"/>
      </linearGradient>
    </defs>
    <path role="img" aria-label="Photo of a smiling patient in a dental chair with a hygienist holding a dental tool" d="M150 28 L410 28 L410 210 Q300 290 170 272 Q60 256 0 190 L0 110 Q70 60 150 28 Z" fill="url(#clinicTones)"/>
    <path d="M0 170 Q100 300 250 282 Q350 266 410 200 L410 525 L0 525 Z" fill="var(--purple)"/>
    <path d="M0 170 Q100 300 250 282 Q350 266 410 200 L410 214 Q340 292 230 300 Q80 302 0 186 Z" fill="var(--purple-deep)"/>
    <rect x="0" y="480" width="410" height="31" fill="var(--green)"/>
    <line x1="0" y1="484" x2="410" y2="484" stroke="#fff" stroke-dasharray="4 3"/>
    <line x1="0" y1="507" x2="410" y2="507" stroke="#fff" stroke-dasharray="4 3"/>
    <rect x="0" y="511" width="410" height="14" fill="var(--purple-night)"/>
  </svg>

  <div class="brand">
    <div class="brand__name"><span class="brand__dot"></span>Smilewagons on Wheels</div>
    <div class="brand__tagline">Mobile Dental Hygienists</div>
  </div>

  <p class="intro">We are a mobile dental hygienist service<br>based in the Teesside area of England</p>

  <div class="call">Call US for<span class="call__big">more</span>information</div>
  <div class="phone-btn">
    <span class="phone-btn__icon">
      <svg width="26" height="30" viewBox="0 0 24 24"><path fill="#fff" d="M6.6 10.8a15.1 15.1 0 0 0 6.6 6.6l2.2-2.2c.3-.3.7-.4 1-.2 1.1.4 2.3.6 3.6.6.6 0 1 .4 1 1V20c0 .6-.4 1-1 1A17 17 0 0 1 3 4c0-.6.4-1 1-1h3.5c.6 0 1 .4 1 1 0 1.3.2 2.5.6 3.6.1.3 0 .7-.2 1l-2.3 2.2z"/></svg>
    </span>
    <span class="phone-btn__rule"></span>
    <span class="phone-btn__number">07812460395</span>
  </div>
  <p class="email">info@smilewagonsonwheels.co.uk</p>
</section>

<section class="flyer flyer--back">
  <svg class="flyer__art" viewBox="0 0 410 525">
    <defs>
      <linearGradient id="nightTones" x1="0" y1="0" x2="0" y2="1">
        <stop offset="0" stop-color="#4a3f33"/>
        <stop offset=".55" stop-color="#8a6a3c"/>
        <stop offset="1" stop-color="#2c241c"/>
      </linearGradient>
    </defs>
    <rect width="410" height="525" fill="var(--purple)"/>
    <path role="img" aria-label="Photo of a lit city bridge over a river at night" d="M0 0 H410 V140 Q300 262 160 246 Q60 234 0 150 Z" fill="url(#nightTones)"/>
    <path d="M0 150 Q60 234 160 246 Q300 262 410 140 L410 156 Q300 276 150 258 Q50 244 0 164 Z" fill="var(--purple-deep)"/>
    <rect x="0" y="480" width="410" height="31" fill="var(--green)"/>
    <line x1="0" y1="484" x2="410" y2="484" stroke="#fff" stroke-dasharray="4 3"/>
    <line x1="0" y1="507" x2="410" y2="507" stroke="#fff" stroke-dasharray="4 3"/>
    <rect x="0" y="511" width="410" height="14" fill="var(--purple-night)"/>
  </svg>

  <div class="about">
    <h2 class="about__title">ABOUT US</h2>
    <p class="about__text">we are a mobile dental hygienist service based in the Teesside area of England.We use portable equipment to treat clients where they live or work</p>
    <p class="about__text">Since may 2013 in the uk hygienists no longer need to work with a dentist ,therefore clients can now access dental hygiene care without seeing a dentist .We offer scale and polish ,oral hygiene advice</p>
  </div>

  <div class="team">
    <div class="team__label">The hygienists names</div>
    <div class="team__names">Moira Palfrey and Janet Ruddock</div>
  </div>

  <div class="call">Call US for<span class="call__big">more</span>information</div>
  <div class="phone-btn">
    <span class="phone-btn__icon">
      <svg width="26" height="30" viewBox="0 0 24 24"><path fill="#fff" d="M6.6 10.8a15.1 15.1 0 0 0 6.6 6.6l2.2-2.2c.3-.3.7-.4 1-.2 1.1.4 2.3.6 3.6.6.6 0 1 .4 1 1V20c0 .6-.4 1-1 1A17 17 0 0 1 3 4c0-.6.4-1 1-1h3.5c.6 0 1 .4 1 1 0 1.3.2 2.5.6 3.6.1.3 0 .7-.2 1l-2.3 2.2z"/></svg>
    </span>
    <span class="phone-btn__rule"></span>
    <span class="phone-btn__number">07812460395</span>
  </div>
  <p class="email">info@smilewagonsonwheels.co.uk</p>
</section>

</body>
</html>
```